BrightWave Tristate Commercial Cleaning Brochure

We need a tri fold brochure that we can use to market our commercial cleaning services to clients. We are looking for something that will stand out. We don't want to use any faces of people on the brochures, only cleaning tools and supplies. We offer Office Cleaning, Covid Cleaning, Janitorial and Floor Services

Target Market(s)

Small to large businesses

Industry/Entity Type

Commercial Cleaning

Colors
0054AA
0677BA
7BADD7
CADEEF
E8F1F8
0094D4
00A9DD
6FCCEA
C7EBF8
E9F6FB
00AB8E
00BBA5
67D7C9
C6EFE9
E9F9F6
59FF00
82FF00
B8FF75
E3FFCB
F4FFEA

Requirements
Must have
• Stand out design-Eye Catching
Should not have
• faces of ppl the brochure

```html
<!DOCTYPE html>
<html lang="en">
<head>
<meta charset="utf-8">
<title>BrightWave Tristate – Commercial Cleaning Tri-fold</title>
<link href="https://fonts.googleapis.com/css2?family=Quicksand:wght@500;600;700&family=Oswald:wght@500;600&family=Lato:wght@400;700&display=swap" rel="stylesheet">
<style>
  :root{
    --bg:#8a8a8a;
    --green:#84c13d;
    --green-text:#7ab631;
    --blue:#1a52a5;
    --blue-dark:#0f3f86;
    --white:#ffffff;
    --ink:#1d1d1d;
    --star:#f7c21b;
  }
  *{box-sizing:border-box;margin:0;padding:0}
  html,body{width:1200px;height:1200px;overflow:hidden;background:var(--bg)}
  body{position:relative;font-family:'Lato',sans-serif;color:var(--ink)}

  .spread{position:absolute;left:240px;width:720px;height:556px;overflow:hidden;
    box-shadow:0 4px 14px rgba(0,0,0,.25)}
  .spread--outside{top:28px;background:linear-gradient(90deg,#fff 0,#fff 230px,#eceeef 230px,#fafafa 400px,#fff 472px,#ececec 472px,#fff 720px)}
  .spread--inside{top:616px;background:linear-gradient(90deg,#fff 0,#e9eaeb 230px,#fafafa 440px,#fff 490px,#fff 720px)}

  .abs{position:absolute}
  .center{text-align:center}
  .layer{position:absolute;inset:0}

  .script-heading{font-family:'Quicksand',sans-serif;font-weight:600;color:var(--blue);font-size:22px;line-height:1}
  .swoosh{position:absolute}

  .brand{position:absolute;font-family:'Quicksand',sans-serif;font-weight:700;color:var(--blue);text-align:center;line-height:1}
  .brand__name{display:block}
  .brand__region{display:block;text-align:right;padding-right:4px}

  .testimonial{position:absolute;left:14px;width:202px;text-align:center}
  .testimonial__stars{color:var(--star);font-size:10px;letter-spacing:3px;line-height:1}
  .testimonial__quote{font-size:10.5px;line-height:13px;margin-top:5px;position:relative;padding:0 10px}
  .testimonial__quote::before{content:"\201C";position:absolute;left:-2px;top:-4px;font-size:20px;font-family:Georgia,serif}
  .testimonial__quote::after{content:"\201D";position:absolute;right:-2px;bottom:-10px;font-size:20px;font-family:Georgia,serif}
  .testimonial__name{font-size:8.5px;margin-top:4px}

  .offer{position:absolute;left:21px;top:402px;width:184px;height:129px;background:var(--blue);
    border-radius:0 0 14px 14px;color:var(--white);text-align:center;font-family:'Oswald',sans-serif;font-weight:600;white-space:nowrap}
  .offer__big{position:absolute;left:0;right:0;top:36px;font-size:44px;line-height:1}
  .offer__small{position:absolute;left:0;right:0;top:92px;font-size:19px;line-height:1;font-weight:500}

  .call-line{font-family:'Quicksand',sans-serif;font-weight:600;color:var(--blue);font-size:17px;line-height:22px}
  .phone-number{font-family:'Oswald',sans-serif;font-weight:500;color:var(--ink);font-size:26px;line-height:1;letter-spacing:.3px;white-space:nowrap}

  .contact{position:absolute;color:var(--white);text-align:center;font-size:11px;line-height:13px}
  .contact--small{font-size:9.5px;line-height:12px}

  .url-pill{position:absolute;height:22px;background:var(--blue);border-radius:11px;color:var(--white);
    font-family:'Quicksand',sans-serif;font-weight:600;font-size:10px;letter-spacing:1.1px;white-space:nowrap;
    display:flex;align-items:center;justify-content:center}

  .headline{position:absolute;left:472px;width:248px;text-align:center;color:var(--white);white-space:nowrap}
  .headline__bold{font-family:'Oswald',sans-serif;font-weight:600;font-size:27px;line-height:31px}
  .headline__light{font-family:'Quicksand',sans-serif;font-weight:600;font-size:26px;line-height:1;margin-top:3px}

  .about{position:absolute;left:23px;top:94px;width:190px;color:var(--white);font-size:13.5px;line-height:17px}
  .service{position:absolute;width:230px;text-align:center;color:var(--green-text);font-weight:700;font-size:17px;line-height:21px}
  .service-icon{position:absolute}
  .icon-blank{position:absolute;background:var(--blue);border-radius:8px;opacity:.9}
</style>
</head>
<body>

<section class="spread spread--outside" aria-label="Brochure outside spread">
  <div role="img" aria-label="Photo: gloved hands with spray bottle and window squeegee" class="abs"
       style="left:0;top:286px;width:230px;height:130px;background:linear-gradient(135deg,#f3e65a 0%,#e9ecf0 45%,#8fc3ea 75%,#f2f3f5 100%);opacity:.9"></div>
  <div role="img" aria-label="Photo: green bucket filled with cleaning supplies, brushes and cloths" class="abs"
       style="left:472px;top:93px;width:248px;height:290px;background:linear-gradient(160deg,#f1ece4 0%,#e86aa5 28%,#7fbf3b 55%,#3e8fd1 75%,#b0864f 100%);opacity:.85"></div>

  <svg class="layer" viewBox="0 0 720 556" preserveAspectRatio="none" aria-hidden="true">
    <path d="M0,378 C90,395 160,412 240,416 C330,420 400,400 472,372 C520,354 560,342 600,348 C650,356 690,372 720,385 L720,556 L0,556 Z" fill="var(--blue)"/>
    <path d="M0,420 C90,438 160,448 240,446 C330,444 400,418 472,394 C520,378 560,368 600,372 C650,378 690,392 720,402 L720,556 L0,556 Z" fill="var(--green)"/>
  </svg>

  <div class="script-heading abs center" style="left:0;width:230px;top:24px;font-size:21px">Testimonials</div>
  <svg class="swoosh" style="left:50px;top:48px" width="130" height="18" viewBox="0 0 130 18" aria-hidden="true"><path d="M2,8 C40,18 90,16 128,6" stroke="var(--blue)" stroke-width="3" fill="none" stroke-linecap="round"/></svg>

  <div class="testimonial" style="top:93px">
    <div class="testimonial__stars">★★★★★</div>
    <p class="testimonial__quote">Lorem ipsum dolor sit amet</p>
    <p class="testimonial__name">- The client's name</p>
  </div>
  <div class="testimonial" style="top:153px">
    <div class="testimonial__stars">★★★★★</div>
    <p class="testimonial__quote">Lorem ipsum dolor sit amet, consectetur adipiscing elit, sed do eiusmod tempor</p>
    <p class="testimonial__name">- The client's name</p>
  </div>
  <div class="testimonial" style="top:235px">
    <div class="testimonial__stars">★★★★★</div>
    <p class="testimonial__quote">Lorem ipsum dolor sit amet, consectetur adipiscing</p>
    <p class="testimonial__name">- The client's name</p>
  </div>

  <div class="offer">
    <div class="offer__big">20% OFF</div>
    <div class="offer__small">ON FIRST CLEANING</div>
  </div>

  <div class="brand" style="left:272px;width:150px;top:118px;font-size:25px">
    <span class="brand__name">BrightWave</span>
    <span class="brand__region" style="font-size:14px">Tristate</span>
  </div>
  <div class="call-line abs center" style="left:230px;width:242px;top:176px">Call Us today for more<br>information</div>
  <svg class="swoosh" style="left:286px;top:228px" width="130" height="18" viewBox="0 0 130 18" aria-hidden="true"><path d="M2,6 C40,16 90,16 128,6" stroke="var(--blue)" stroke-width="3" fill="none" stroke-linecap="round"/></svg>
  <svg class="abs" style="left:341px;top:262px" width="14" height="20" viewBox="0 0 14 20" aria-hidden="true"><path d="M4,1 L7,1 L8,6 L5,8 C6,11 7,13 9,14 L11,12 L13,15 L12,19 C6,19 1,12 2,4 Z" fill="var(--green)"/></svg>
  <div class="phone-number abs center" style="left:230px;width:242px;top:291px">+1 555-014-2288</div>

  <svg class="abs" style="left:346px;top:434px" width="10" height="7" viewBox="0 0 10 7" aria-hidden="true"><rect x=".5" y=".5" width="9" height="6" fill="var(--white)"/><path d="M.5,.5 L5,4 L9.5,.5" stroke="var(--green)" fill="none"/></svg>
  <div class="contact" style="left:230px;width:242px;top:445px">info@brightwavetristate.com</div>
  <svg class="abs" style="left:346px;top:466px" width="10" height="10" viewBox="0 0 10 10" aria-hidden="true"><circle cx="5" cy="5" r="4.2" stroke="var(--white)" fill="none"/><path d="M5,2.5 V5 H7" stroke="var(--white)" fill="none"/></svg>
  <div class="contact contact--small" style="left:230px;width:242px;top:481px">Monday- Friday : 9:00am-5:00pm<br>Saturday &amp; Sunday : CLOSED</div>
  <div class="url-pill" style="left:257px;width:183px;top:515px">www.brightwavetristate.com</div>

  <div class="brand" style="left:514px;width:166px;top:36px;font-size:29px">
    <span class="brand__name">BrightWave</span>
    <span class="brand__region" style="font-size:16px">Tristate</span>
  </div>
  <div class="headline" style="top:404px">
    <div class="headline__bold">YOUR TOP RATED<br>TRISTATE COMMERCIAL</div>
    <div class="headline__light">Cleaning Team</div>
  </div>
  <div class="url-pill" style="left:506px;width:182px;top:515px">www.brightwavetristate.com</div>
</section>

<section class="spread spread--inside" aria-label="Brochure inside spread">
  <svg class="layer" viewBox="0 0 720 556" preserveAspectRatio="none" aria-hidden="true">
    <path d="M0,0 L283,0 C250,80 220,180 225,262 C230,340 250,420 238,480 C230,510 216,535 212,556 L0,556 Z" fill="var(--green)"/>
    <path d="M283,0 C250,80 220,180 225,262 C230,340 250,420 238,480 C230,510 216,535 212,556" fill="none" stroke="var(--blue)" stroke-width="12" transform="translate(6,0)"/>
  </svg>

  <div class="script-heading abs center" style="left:0;width:225px;top:28px">About us</div>
  <svg class="swoosh" style="left:45px;top:54px" width="135" height="18" viewBox="0 0 135 18" aria-hidden="true"><path d="M2,8 C40,18 95,16 133,6" stroke="var(--blue)" stroke-width="3" fill="none" stroke-linecap="round"/></svg>
  <p class="about">Lorem ipsum dolor sit amet, consectetur adipiscing elit, sed do eiusmod tempor incididunt ut labore et dolore magna aliqua. Ut enim ad minim veniam, quis nostrud exercitation ullamco laboris nisi ut aliquip ex ea commodo consequat. Duis aute irure dolor in reprehenderit in voluptate velit esse cillum dolore eu fugiat nulla pariatur. Excepteur sint occaecat cupidatat non proident, sunt in culpa qui officia deserunt mollit anim id est laborum.</p>
  <div role="img" aria-label="Photo: bottles, sponges, gloves and brushes of cleaning supplies" class="abs"
       style="left:0;top:390px;width:215px;height:160px;background:linear-gradient(120deg,#8a5cc4 0%,#e84a6b 30%,#ffffff 50%,#3fb6e0 70%,#f28a2e 100%);opacity:.85;border-radius:0 30px 0 0"></div>

  <div class="script-heading abs center" style="left:470px;width:180px;top:30px">We Provide</div>
  <svg class="swoosh" style="left:485px;top:64px" width="150" height="18" viewBox="0 0 150 18" aria-hidden="true"><path d="M2,6 C45,16 105,16 148,6" stroke="var(--blue)" stroke-width="3" fill="none" stroke-linecap="round"/></svg>

  <svg class="service-icon" style="left:337px;top:103px" width="50" height="44" viewBox="0 0 50 44" aria-hidden="true">
    <circle cx="20" cy="22" r="17" fill="none" stroke="var(--blue)" stroke-width="3.5"/>
    <path d="M20,12 V23 H28" fill="none" stroke="var(--blue)" stroke-width="3.5" stroke-linecap="round"/>
    <text x="33" y="42" font-family="Lato,sans-serif" font-weight="700" font-size="22" fill="var(--blue)">$</text>
  </svg>
  <div class="service" style="left:246px;top:156px">Free Estimates</div>
  <div class="icon-blank" role="img" aria-label="Icon: cleaning staff member with broom" style="left:344px;top:198px;width:34px;height:46px"></div>
  <div class="service" style="left:246px;top:251px">Fully Trained Staff</div>
  <div class="icon-blank" role="img" aria-label="Icon: spray bottle and bucket with sparkles" style="left:340px;top:302px;width:44px;height:44px"></div>
  <div class="service" style="left:246px;top:354px">Regular or one-time<br>cleaning</div>
  <div class="icon-blank" role="img" aria-label="Icon: broom sweeping" style="left:340px;top:422px;width:44px;height:44px"></div>
  <div class="service" style="left:246px;top:479px">Customized Cleaning<br>services</div>

  <div class="icon-blank" role="img" aria-label="Icon: cleaning cart with supplies and equipment" style="left:580px;top:97px;width:44px;height:50px"></div>
  <div class="service" style="left:487px;top:155px">All supplies and<br>equipment provided</div>
  <svg class="service-icon" style="left:582px;top:217px" width="42" height="48" viewBox="0 0 42 48" aria-hidden="true">
    <path d="M21,2 L36,8 V20 C36,29 29,35 21,38 C13,35 6,29 6,20 V8 Z" fill="none" stroke="var(--blue)" stroke-width="3.5"/>
    <path d="M14,20 L19,25 L28,15" fill="none" stroke="var(--blue)" stroke-width="3.5" stroke-linecap="round"/>
    <path d="M2,44 C10,38 20,40 26,42 L40,38" fill="none" stroke="var(--blue)" stroke-width="3.5" stroke-linecap="round"/>
  </svg>
  <div class="service" style="left:487px;top:279px">Bonded and insured</div>
  <div class="icon-blank" role="img" aria-label="Icon: staff member mopping the floor" style="left:582px;top:320px;width:40px;height:46px"></div>
  <div class="service" style="left:487px;top:383px">Cleared staff</div>

  <div class="brand" style="left:520px;width:150px;top:430px;font-size:27px">
    <span class="brand__name">BrightWave</span>
    <span class="brand__region" style="font-size:15px">Tristate</span>
  </div>
  <div class="call-line abs center" style="left:487px;width:230px;top:481px;font-size:14px;line-height:17px">Call Us today for more<br>information</div>
  <div class="abs" style="left:528px;top:519px;display:flex;align-items:center;gap:3px">
    <svg width="12" height="18" viewBox="0 0 14 20" aria-hidden="true"><path d="M4,1 L7,1 L8,6 L5,8 C6,11 7,13 9,14 L11,12 L13,15 L12,19 C6,19 1,12 2,4 Z" fill="var(--green)"/></svg>
    <span class="phone-number" style="font-size:22px">+1 555-014-2288</span>
  </div>
</section>

</body>
</html>
```